Creating business cards for our new private medical clinic in London

Hey everyone,

We are starting a new private medical clinic in central London. We already have our logo (please see the 2 different layouts of the logo attached.) Please note that we are not restricted to using only this font in the card though.

The cards will be printed by "Pekko." The cards have a textured surface and a coloured middle layer - please see this webpage for the exact product spec (https://www.pekkoprint.example/uk/products/velvet/business-cards.html). We're overall looking for a modern yet highly professional look. We'd like the cards to have Square edges and NOT rounded please.

We need a standard card that uses one or both of our logo's colours (blue and green), and another card for premium customers, that uses black with either gold/silver/bronze. On the black coloured cads, please could you add the word "Black Account" or the word "Black" under the logo text - wherever you think it looks best?

_________________

AMENDMENT TO BRIEF:

1) The first batch of our cards are to be promotional cards and need to have more information. Could please have one card that is more like an "information card" that has the following information: - (There's a lot there and we might need to slim this down once we see the cards.)

GP appointments £70
-Feeling unwell
-Referrals to private specialists
-Sexual health check up
-Contraception
-Second opinion

Launch Offer
First appointment £40 with this card until 30 September 2017

Book online

2) Could you see whether we could add a 'strap line' to the card, something like: “Stay in Optimal Health”

_____________

The files attached have 2 versions of our logo - one linear and with the words 'stacked'; we think that the stacked logo may work better for the business card but we'd love to see different versions.

On one side of the card could we please see a coloured background, with a design containing our logo? On the other side of the card, please could we have a different coloured or white background and the information below.

Address: THE HARROWFIELD CLINIC @ FitVanta, 19 Bramblecote Lane, London, EC2Z 4QJ
Open: Mon-Fri (early & late appointments)
Book Online: www.harrowfieldclinic.example
Email: bookings@harrowfieldclinic.example
Phone number: (We don't have this yet - but please leave a space for this to go into.)

Other possible design features:

Because our clinic is located in the financial district of London, anything that represents this (e.g. The City of London's skyline - i.e. financial district - could look nice (example buildings include: The Pinecone, The Teacup-Tower, The Wedgehouse, St Aldric Minster, Keep of Brennmoor, Gantry Crossing, The Spindle). We wondered whether a outline or drawing of these buildings in the background of the card could look nice. Please see the image link below to get an idea of the skyline we're looking for:

https://img.stockvale.example/z/skyline-hand-drawn-city-pastel-shades-heritage-buildings-futuristic-81920457.jpg

The following image links are examples of cards that we've seen online and like the overall feel of (of course our colours are different):

http://www.craftnook.example/diverse/2/goodcards/73014589122.jpg
http://cardheron.example/wp-content/uploads/2013/01/cool-business-cards-saffron.jpg
https://cardfolio.example/wp-content/uploads/20461-cool-business-card-mockup.jpg
http://www.plinthworks.example/wp-content/uploads/edd/2015/08/Modern-Tutor-Business-Card-Template-Preview.jpg
http://lorvelandkit.example/wp-content/uploads/2017/01/design-a-business-card-cool-business-card-designsqx83.jpg
http://makerspindle.example/resources/files/articles/harbor-print/copper-foil-business-cards.jpg

STATIONARY:
We will also need the following stationary designed by our chosen designer. We’d like stationary to use one or both the colours of our logo (ie Green and Blue). Please use these colours to add any additional design features to stationary - other similar palette colours can also be used. Our logo font is - abeatbyKai - and this could be used in other parts of the stationary, but please feel free to try other fonts too. We prefer sans serif fonts.

Overall - we are open to all ideas but we need a look and feel that looks modern and highly professional. For our letter, prescription and medical report templates we need these to be PDFs and word processing files that can merge relevant data and text into different sections.

The information required on various pieces of stationary are as follows:

Letterheads:
These need to have:
Clinic's: Logo / Address / Phone Number / Website / Email address / Recipients address.
The letter can have address data either at the top or as a footer. We're happy to see designs that use either to see which one looks best (same goes for other pieces of stationary too.)

Invoices:
Invoice number: (Unique code for document)
Invoice Date:
Clinic’s: Logo / Address / Phone Number / Website / Email address
Services: Service Code / Name of Service / Price
Total Price:
PAYLO, Cardwise and Northern Remit Logos
Patient details: Patient’s Name / Address

Prescription Pads:
Prescription number: (Unique code for document)
Clinic details: Clinic’s Logo / Address / Phone Number / Website / Email address
Patient details needed include: Patient’s Name / Date of birth / address
Blank space required to write the name of medication
Doctors Signature: and space for signature
MPB Number: and space for this to be entered

Templates for our medical reports:
These are reports we will be printed (on good quality paper) for patients after they have had a complete health check. They will include a text summary, and the results of any tests (with graphs) and images of scans. Please could we see how text/titles/headings/tables etc could be styled?
They will need the following details: -
Clinic details needed include: Clinic’s Logo / Address / Phone Number / Website / Email address
Date of Report:
Then the following sections need to be includes:
1) Free Text Space
2) Space for images and text
3) Space for blood test and text

___________________

Thanks so much everyone.

All the best,

Tev and Dane

Target Market(s)

City of London
Private Healthcare

Industry/Entity Type

Health Care

Contact Information for Business Card

Font styles to use
Sans Serif

Colors
33a6d7
25a0d3
add136
9bcb3c
cadf82
85acd3
3276b5
0255a3
85cae6

Requirements
Must have
• Please see project description for details.
Nice to have
• Perhaps a outline/drawing/illustration of the City of London skyline (i.e. the Pinecone and surrounding buildings)

```html
<!DOCTYPE html>
<html lang="en">
<head>
<meta charset="utf-8">
<title>The Harrowfield Clinic – Business Card</title>
<link rel="stylesheet" href="https://fonts.googleapis.com/css2?family=Open+Sans:wght@400;600;700&display=swap">
<style>
  :root {
    --backdrop: #1c1c1c;
    --card: #2a2a2a;
    --card-edge: #333333;
    --blue: #33a6d7;
    --band-blue: #4cb6e0;
    --green: #add136;
    --grey-text: #c9c9c9;
    --muted: #8a8a8a;
    --emboss: #4a4a4a;
    --white: #ffffff;
  }
  * { box-sizing: border-box; margin: 0; padding: 0; }
  html, body {
    width: 1200px; height: 1000px; overflow: hidden;
    background: var(--backdrop);
    font-family: "Open Sans", Arial, sans-serif;
  }
  .sheet {
    position: relative; width: 1200px; height: 1000px;
    display: flex; flex-direction: column; align-items: center;
    justify-content: center; gap: 40px;
  }
  .card {
    position: relative; width: 680px; height: 440px;
    background: var(--card);
    border: 1px solid var(--card-edge);
    overflow: hidden;
  }

  /* Front side */
  .card--front .brand {
    position: absolute; left: 0; right: 0; top: 170px;
    display: flex; align-items: center; justify-content: center; gap: 16px;
  }
  .brand-mark {
    width: 38px; height: 38px; background: var(--emboss);
  }
  .card--front .brand-name {
    display: block; white-space: nowrap;
    font-size: 40px; font-weight: 400; color: var(--emboss);
    letter-spacing: 0.5px; line-height: 1;
  }
  .card--front .brand-tag {
    display: block; margin-top: 6px; text-align: right;
    font-size: 10px; font-weight: 700; letter-spacing: 2px; color: var(--emboss);
  }

  /* Back side */
  .card--back .brand {
    position: absolute; left: 24px; top: 178px; width: 270px; text-align: right;
  }
  .card--back .brand-name {
    display: block; white-space: nowrap;
    font-size: 22px; font-weight: 400; color: var(--blue); line-height: 1.1;
  }
  .card--back .brand-tag {
    display: block; margin-top: 5px; white-space: nowrap;
    font-size: 8px; font-weight: 700; letter-spacing: 1.5px; color: var(--muted);
  }
  .divider {
    position: absolute; left: 310px; top: 162px; width: 2px; height: 90px;
    background: var(--muted);
  }
  .contacts {
    position: absolute; left: 328px; top: 162px; list-style: none;
  }
  .contacts li {
    display: flex; align-items: center; gap: 12px; white-space: nowrap;
    height: 30px; font-size: 14px; color: var(--grey-text);
  }
  .contacts svg { width: 13px; height: 13px; flex: none; }
  .book-online {
    margin-left: -4px; font-size: 11px; font-weight: 700; color: var(--green);
    white-space: nowrap;
  }
  .hours {
    position: absolute; left: 175px; top: 300px; white-space: nowrap;
    font-size: 15px; color: var(--grey-text);
  }
  .footer-strip {
    position: absolute; left: 0; right: 0; bottom: 40px; height: 70px;
  }
  .accent-square {
    position: absolute; left: 0; top: 0; width: 40px; height: 40px;
    background: var(--green);
  }
  .mark-square {
    position: absolute; left: 48px; top: 44px; width: 22px; height: 22px;
    background: var(--blue);
  }
  .address-band {
    position: absolute; left: 80px; right: 0; top: 40px; height: 30px;
    background: var(--band-blue); white-space: nowrap;
    display: flex; align-items: center; padding-left: 16px;
    font-size: 14px; color: var(--white);
  }
</style>
</head>
<body>
<main class="sheet">

  <section class="card card--front" aria-label="Card front">
    <div class="brand">
      <span class="brand-mark"></span>
      <div>
        <span class="brand-name">The Harrowfield Clinic</span>
        <span class="brand-tag">PRIVATE GENERAL PRACTICE</span>
      </div>
    </div>
  </section>

  <section class="card card--back" aria-label="Card back">
    <div class="brand">
      <span class="brand-name">The Harrowfield Clinic</span>
      <span class="brand-tag">PRIVATE GENERAL PRACTICE</span>
    </div>
    <span class="divider"></span>
    <ul class="contacts">
      <li>
        <svg viewBox="0 0 16 16" aria-hidden="true"><path fill="#33a6d7" d="M3 1l3 3-1.5 2a9 9 0 005.5 5.5L12 10l3 3-2 2C7 15 1 9 1 3z"/></svg>
        +000 123 456 789
      </li>
      <li>
        <svg viewBox="0 0 16 16" aria-hidden="true"><rect x="1" y="3" width="14" height="10" fill="#33a6d7"/><path d="M1 3l7 6 7-6" fill="none" stroke="#2a2a2a" stroke-width="1.4"/></svg>
        booking@harrowfieldclinic.example
      </li>
      <li>
        <svg viewBox="0 0 16 16" aria-hidden="true"><circle cx="8" cy="8" r="7" fill="#33a6d7"/><path d="M1 8h14M8 1c-3 3-3 11 0 14M8 1c3 3 3 11 0 14" fill="none" stroke="#2a2a2a" stroke-width="1"/></svg>
        <span>www.harrowfieldclinic.example</span>
        <span class="book-online">(Book Online)</span>
      </li>
    </ul>
    <p class="hours">Open: Mon-Fri (early &amp; 10am-8pm Last Appointments)</p>
    <div class="footer-strip">
      <span class="accent-square"></span>
      <span class="mark-square"></span>
      <div class="address-band">The Harrowfield Clinic @ FitVanta, 19 Bramblecote Lane, London, EC2Z 4QJ</div>
    </div>
  </section>

</main>
</body>
</html>
```